Marolina Swimming & Athletics Center

We need Business Card for a Athletics center
The logo frome the Uploaded Files ( b card fimal)
Οn one side of card we need the logo of company the Contact and the website:
1. Address:(Limassol, Cyprus 12-14 Dravelonos str,Ano Feralia,P.C. 5280)

2.Phone number: (+357) 25-804273

3. Mail: info@marolinasport.example

3. Website: www.marolinasport.example

Οn the other side of the card we need to write the sport of the company:

1. Artistic Gymnastics
2. Swimming
3. Gym - Fitness
4. Programs
5. Dancing
5.Tennis

From the Uploaded Files you can get the logo.In a logo is behind the black color which can be removed from logo.

Υou can use that color you want.
.

Industry/Entity Type

Business

Font styles to use
Decorative

Colors
0555a3
ffcf3e
3176b5
0692cd
add136
f04a50
000000
cfcfcf
9d9d9d

Requirements
Should not have
• photos with faces
• photo fro the Website:www.marolinasport.example

```html
<!DOCTYPE html>
<html lang="en">
<head>
<meta charset="utf-8">
<title>Marolina Swimming &amp; Athletics Center – Business Card</title>
<link rel="stylesheet" href="https://fonts.googleapis.com/css2?family=Archivo+Black&family=EB+Garamond:wght@400;600;700&display=swap">
<style>
  :root {
    --bg: #2b2b2b;
    --card: #f7f7f7;
    --card-edge: #e4e4e4;
    --accent: #e89a12;
    --ink: #3a3a3a;
    --ink-soft: #555555;
    --mark: #111111;
    --mark-ring: #c9a53a;
  }
  * { box-sizing: border-box; margin: 0; padding: 0; }
  html, body { width: 1200px; height: 873px; overflow: hidden; }
  body {
    background: var(--bg);
    font-family: "EB Garamond", Georgia, serif;
    color: var(--ink);
    position: relative;
  }
  .card {
    position: absolute;
    top: 276px;
    width: 540px;
    height: 320px;
    background: linear-gradient(160deg, #ffffff 0%, var(--card) 60%, var(--card-edge) 100%);
    border-radius: 18px;
    box-shadow: 0 12px 30px rgba(0,0,0,.45);
  }
  .card--services { left: 40px; }
  .card--contact { left: 620px; }

  .brand {
    position: absolute;
    display: flex;
    align-items: center;
    gap: 14px;
  }
  .brand__name {
    font-family: "Archivo Black", "Arial Black", sans-serif;
    font-weight: 400;
    font-size: 46px;
    letter-spacing: 1px;
    color: var(--accent);
    line-height: 1;
  }
  .brand__dot {
    width: 54px; height: 54px;
    border-radius: 50%;
    background: var(--mark);
    border: 2px solid var(--mark-ring);
  }
  .card--services .brand { left: 60px; top: 58px; }
  .card--contact .brand { right: 40px; top: 36px; }

  .card--services .rule {
    position: absolute; height: 2px; background: var(--accent);
    left: 60px; width: 370px; top: 128px;
  }

  .website {
    position: absolute; left: 60px; width: 370px; top: 136px;
    text-align: center;
    font-size: 15px; color: var(--ink-soft);
  }
  .services {
    position: absolute; left: 45px; top: 180px; width: 400px;
    list-style: none; text-align: center;
    font-size: 19px; line-height: 1.6; color: var(--ink-soft);
  }
  .services .sep { color: var(--accent); padding: 0 6px; }

  .person { position: absolute; left: 40px; right: 40px; top: 112px; }
  .person__row { display: flex; align-items: flex-end; gap: 8px; }
  .person__name { font-size: 22px; font-weight: 600; color: var(--accent); line-height: 1.1; white-space: nowrap; }
  .person__line { flex: 1; height: 2px; background: var(--accent); margin-bottom: 5px; }
  .person__role { font-size: 16px; color: var(--ink-soft); margin-top: 2px; }

  .company {
    position: absolute; right: 40px; top: 150px; text-align: left;
    font-size: 15px; line-height: 1.3; color: var(--ink-soft);
  }
  .company__name { font-size: 17px; font-weight: 600; color: var(--accent); }

  .contact-list {
    position: absolute; left: 40px; bottom: 36px; list-style: none;
    font-size: 17px; line-height: 1.6; color: var(--ink-soft);
  }
  .contact-list li { display: flex; align-items: center; gap: 10px; }
  .contact-list svg { width: 14px; height: 14px; fill: var(--accent); }
</style>
</head>
<body>
  <section class="card card--services" aria-label="Card front: sports offered">
    <div class="brand">
      <span class="brand__name">MAROLINA</span>
      <span class="brand__dot"></span>
    </div>
    <div class="rule"></div>
    <p class="website">www.marolinasport.example</p>
    <ul class="services">
      <li>Artistic Gymnastics<span class="sep">•</span>Swimming</li>
      <li>Gym<span class="sep">•</span>Fitness Programs</li>
      <li>Dancing<span class="sep">•</span>Tennis</li>
    </ul>
  </section>

  <section class="card card--contact" aria-label="Card back: contact details">
    <div class="brand">
      <span class="brand__name">MAROLINA</span>
      <span class="brand__dot"></span>
    </div>
    <div class="person">
      <div class="person__row">
        <p class="person__name">Daniel Harper</p>
        <span class="person__line"></span>
      </div>
      <p class="person__role">Owner / Founder</p>
    </div>
    <div class="company">
      <p class="company__name">Marolina Pvt Ltd.</p>
      <p>Limassol, Cyprus 12-14</p>
      <p>Ano Feralia,P.C. 5280</p>
    </div>
    <ul class="contact-list">
      <li>
        <svg viewBox="0 0 16 16" aria-hidden="true"><path d="M2 5c0-2 2-3 6-3s6 1 6 3v1h-3V5H5v1H2zM4 7h8l2 7H2z"/></svg>
        (+357) 25-804273
      </li>
      <li>
        <svg viewBox="0 0 16 16" aria-hidden="true"><path d="M1 3h14v10H1zM2 4l6 5 6-5z"/></svg>
        info@marolinasport.example
      </li>
    </ul>
  </section>
</body>
</html>
```